" Nosso escritório de advocacia atende a empresas diversas, oferecendo serviços de consultoria na área trabalhista, orientação para defesa em fiscalizações, defesas em processos administrativos e judiciais trabalhistas, sempre focado no cuidado com as necessidades pessoais dos clientes e do seu patrimônio. "

```html
<!DOCTYPE html>
<html lang="pt-BR">
<head>
<meta charset="utf-8">
<title>Assinatura de e-mail – Bastos Lima Advocacia</title>
<link rel="stylesheet" href="https://fonts.googleapis.com/css2?family=Tinos&family=Tenor+Sans&display=swap">
<style>
  :root {
    --page-bg: #dcdddf;
    --band-navy: #183253;
    --text-light: #ffffff;
    --divider: #8193a8;
  }
  * { margin: 0; padding: 0; box-sizing: border-box; }
  html, body {
    width: 1200px;
    height: 1200px;
    overflow: hidden;
    background: var(--page-bg);
  }
  .canvas {
    position: relative;
    width: 1200px;
    height: 1200px;
  }
  .signature-band {
    position: absolute;
    left: 60px;
    top: 415px;
    width: 1080px;
    height: 250px;
    background: var(--band-navy);
    color: var(--text-light);
  }
  .firm-name {
    position: absolute;
    left: 72px;
    top: 70px;
    width: 360px;
    text-align: center;
    font-family: "Tenor Sans", sans-serif;
    font-size: 34px;
    line-height: 1.25;
    letter-spacing: 4px;
    text-transform: uppercase;
  }
  .firm-name .firm-mark {
    display: inline-block;
    width: 14px;
    height: 14px;
    background: var(--text-light);
    margin-right: 12px;
    vertical-align: middle;
  }
  .divider {
    position: absolute;
    left: 529px;
    top: 29px;
    width: 2px;
    height: 192px;
    background: var(--divider);
  }
  .contact-block {
    position: absolute;
    left: 590px;
    top: 50px;
    width: 415px;
    text-align: center;
  }
  .person-name,
  .person-role {
    font-family: "Tinos", serif;
    font-size: 25px;
    line-height: 30px;
  }
  .contact-list {
    list-style: none;
    margin-top: 20px;
    font-family: "Tenor Sans", sans-serif;
    font-size: 19px;
    line-height: 27px;
  }
  .contact-phone { letter-spacing: 3px; }
</style>
</head>
<body>
  <div class="canvas">
    <section class="signature-band">
      <p class="firm-name"><span class="firm-mark"></span>Bastos Lima<br>Advocacia</p>
      <div class="divider"></div>
      <div class="contact-block">
        <p class="person-name">Nome Sobrenome</p>
        <p class="person-role">Cargo</p>
        <ul class="contact-list">
          <li class="contact-phone">Fone: (99) 9999-9999</li>
          <li class="contact-email">contato@bastoslima.adv.br</li>
          <li class="contact-web">www.bastoslima.adv.br</li>
        </ul>
      </div>
    </section>
  </div>
</body>
</html>
```